Banner Ad Design Project

We are a SEO company and need a banner design for our new service, the highlights being:

- Pay Per Performance SEO service
- Guaranteed Zumbly page 1 ranking
- Only $197 per month (+ performance bonus)

Can be all on one static banner or made into an animated GIF - designers choice...

Site URL (not up yet) will be RankNest412.com (by velHelm) - this is a spinoff site of our existing business, velHelm LLC - logo attached and should be included on the banner.

Industry/Entity Type

Business

Requirements
Must have
• Banner delivered in multiple sizes:
- 200 x 200
- 250 x 250
- 300 x 250
- 336 x 280
- 468 x 60
- 728 x 90
- 120 x 600
- 160 x 600

```html
<!DOCTYPE html>
<html lang="en">
<head>
<meta charset="utf-8">
<title>velHelm – Pay Per Performance SEO banner set</title>
<link rel="stylesheet" href="https://fonts.googleapis.com/css2?family=Open+Sans:wght@400;600;700&display=swap">
<style>
:root{
  --page:#ffffff;
  --blue-deep:#0b22a0;
  --blue-mid:#1f5fd0;
  --blue-sky:#45b4ea;
  --white:#ffffff;
  --swoosh-orange:#f08a1c;
  --swoosh-red:#d8262a;
  --logo-green:#7cc142;
  --logo-blue:#1f4fb8;
  --button-top:#fbfbfb;
  --button-bottom:#c9c9c9;
  --button-text:#222222;
  --frame:#9a9a9a;
  --photo-light:#e7c9b4;
  --photo-dark:#2a2a33;
}
*{box-sizing:border-box;margin:0;padding:0}
html,body{width:1200px;height:573px;overflow:hidden;background:var(--page)}
body{position:relative;font-family:"Open Sans",Arial,sans-serif}

.banner{position:absolute;overflow:hidden;border:1px solid var(--frame);background:var(--white);color:var(--white)}
.banner-bg{position:absolute;inset:0;width:100%;height:100%}
.banner > *:not(.banner-bg){position:absolute}

.headline{font-weight:600;line-height:.95;letter-spacing:-.01em;text-shadow:0 1px 2px rgba(0,0,0,.35)}
.highlights{list-style:none;font-weight:400;line-height:1.15}
.highlights li{margin-bottom:.45em}
.cta{display:flex;align-items:center;justify-content:center;font-weight:600;color:var(--button-text);
  background:linear-gradient(var(--button-top),var(--button-bottom));border:1px solid #8d8d8d;box-shadow:0 1px 2px rgba(0,0,0,.4)}
.agent-photo{background:linear-gradient(170deg,var(--photo-light) 0%,#c9a087 45%,var(--photo-dark) 75%);border-radius:45% 45% 0 0}
.brand{display:flex;align-items:center;font-weight:600;color:var(--logo-blue);letter-spacing:-.01em}
.brand-dot{border-radius:50%;background:var(--logo-green);flex:none}

/* skyscraper 120 x 600 */
.sky-wide{left:112px;top:66px;width:102px;height:376px}
.sky-wide .headline{left:8px;top:40px;font-size:20px}
.sky-wide .highlights{left:5px;top:86px;width:94px;font-size:8.5px}
.sky-wide .cta{left:8px;top:191px;width:64px;height:16px;font-size:8.5px}
.sky-wide .agent-photo{left:32px;top:210px;width:66px;height:108px}
.sky-wide .brand{left:8px;top:342px;font-size:17px;gap:4px}
.sky-wide .brand-dot{width:22px;height:22px}

/* skyscraper 160 x 600 */
.sky-narrow{left:230px;top:66px;width:77px;height:376px}
.sky-narrow .headline{left:5px;top:28px;font-size:16px}
.sky-narrow .highlights{left:3px;top:67px;width:72px;font-size:8.5px}
.sky-narrow .cta{left:9px;top:193px;width:58px;height:14px;font-size:8px}
.sky-narrow .agent-photo{left:12px;top:212px;width:62px;height:106px}
.sky-narrow .brand{left:4px;top:345px;font-size:13px;gap:3px}
.sky-narrow .brand-dot{width:18px;height:18px}

/* large rectangle 336 x 280 */
.rect-large{left:329px;top:88px;width:211px;height:176px}
.rect-large .headline{left:20px;top:19px;font-size:16px}
.rect-large .highlights{left:14px;top:43px;width:150px;font-size:8.5px}
.rect-large .cta{left:20px;top:104px;width:65px;height:17px;font-size:8.5px}
.rect-large .agent-photo{left:158px;top:26px;width:53px;height:130px}
.rect-large .brand{left:10px;top:146px;font-size:17px;gap:4px}
.rect-large .brand-dot{width:24px;height:24px}

/* medium rectangle 300 x 250 */
.rect-medium{left:558px;top:107px;width:189px;height:157px}
.rect-medium .headline{left:18px;top:15px;font-size:14px}
.rect-medium .highlights{left:14px;top:33px;width:105px;font-size:7.5px}
.rect-medium .cta{left:20px;top:100px;width:58px;height:13px;font-size:7.5px}
.rect-medium .agent-photo{left:124px;top:18px;width:62px;height:118px}
.rect-medium .brand{left:10px;top:132px;font-size:14px;gap:3px}
.rect-medium .brand-dot{width:19px;height:19px}

/* square 250 x 250 */
.square-large{left:775px;top:107px;width:158px;height:157px}
.square-large .headline{left:14px;top:14px;font-size:12px}
.square-large .highlights{left:10px;top:33px;width:140px;font-size:6.8px}
.square-large .cta{left:15px;top:95px;width:48px;height:11px;font-size:6.3px}
.square-large .agent-photo{left:94px;top:58px;width:62px;height:80px}
.square-large .brand{left:8px;top:134px;font-size:12px;gap:3px}
.square-large .brand-dot{width:16px;height:16px}

/* small square 200 x 200 */
.square-small{left:978px;top:138px;width:127px;height:127px}
.square-small .headline{left:11px;top:11px;font-size:10px}
.square-small .highlights{left:8px;top:27px;width:115px;font-size:5.4px}
.square-small .cta{left:12px;top:74px;width:38px;height:9px;font-size:5px}
.square-small .agent-photo{left:75px;top:46px;width:50px;height:64px}
.square-small .brand{left:6px;top:108px;font-size:10px;gap:2px}
.square-small .brand-dot{width:13px;height:13px}

/* leaderboard 728 x 90 */
.leaderboard{left:331px;top:326px;width:457px;height:58px}
.leaderboard .brand{left:12px;top:17px;font-size:17px;gap:4px}
.leaderboard .brand-dot{width:24px;height:24px}
.leaderboard .headline{left:133px;top:12px;font-size:15px}
.leaderboard .highlights{left:133px;top:31px;font-size:8.5px;line-height:1.2}
.leaderboard .highlights li{margin:0}
.leaderboard .cta{left:375px;top:1px;width:64px;height:15px;font-size:8.5px}

/* banner 468 x 60 */
.banner-full{left:811px;top:336px;width:293px;height:39px}
.banner-full .brand{left:6px;top:11px;font-size:11px;gap:3px}
.banner-full .brand-dot{width:15px;height:15px}
.banner-full .headline{left:86px;top:8px;font-size:10.5px}
.banner-full .highlights{left:86px;top:21px;font-size:5.4px;line-height:1.25}
.banner-full .highlights li{margin:0}
.banner-full .cta{left:235px;top:1px;width:45px;height:10px;font-size:5.5px}
</style>
</head>
<body>

<svg width="0" height="0" style="position:absolute" aria-hidden="true">
  <defs>
    <linearGradient id="sky-vertical" x1="0" y1="0" x2="0" y2="1">
      <stop offset="0" stop-color="#0b22a0"/>
      <stop offset=".5" stop-color="#1f5fd0"/>
      <stop offset="1" stop-color="#45b4ea"/>
    </linearGradient>
    <linearGradient id="sky-horizontal" x1="0" y1="0" x2="1" y2="0">
      <stop offset="0" stop-color="#0b22a0"/>
      <stop offset=".6" stop-color="#1a3fb8"/>
      <stop offset="1" stop-color="#2b6fd4"/>
    </linearGradient>
    <linearGradient id="swoosh" x1="0" y1="0" x2="1" y2="0">
      <stop offset="0" stop-color="#f08a1c"/>
      <stop offset="1" stop-color="#d8262a"/>
    </linearGradient>
    <linearGradient id="brand-stripe" x1="0" y1="0" x2="0" y2="1">
      <stop offset="0" stop-color="#f7c21b"/>
      <stop offset=".5" stop-color="#e8551f"/>
      <stop offset="1" stop-color="#7a1fa0"/>
    </linearGradient>
  </defs>
</svg>

<!-- 120 x 600 -->
<div class="banner sky-wide">
  <svg class="banner-bg" viewBox="0 0 100 100" preserveAspectRatio="none" aria-hidden="true">
    <rect width="100" height="100" fill="url(#sky-vertical)"/>
    <path d="M0,76 Q50,78 100,84 L100,100 L0,100Z" fill="#fff"/>
    <path d="M0,76 Q50,78 100,84" fill="none" stroke="url(#swoosh)" stroke-width="1.2" vector-effect="non-scaling-stroke" style="stroke-width:4px"/>
  </svg>
  <h2 class="headline">NEW<br>SERVICE</h2>
  <ul class="highlights">
    <li>- Pay Per Performance SEO service</li>
    <li>- Guaranteed Zumbly page 1 ranking</li>
    <li>- Only $197 per month (+ performance bonus)</li>
  </ul>
  <span class="cta">Click here</span>
  <div class="agent-photo" role="img" aria-label="Smiling support agent wearing a headset"></div>
  <div class="brand"><span class="brand-dot"></span>velHelm</div>
</div>

<!-- 160 x 600 -->
<div class="banner sky-narrow">
  <svg class="banner-bg" viewBox="0 0 100 100" preserveAspectRatio="none" aria-hidden="true">
    <rect width="100" height="100" fill="url(#sky-vertical)"/>
    <path d="M0,79 Q50,81 100,85 L100,100 L0,100Z" fill="#fff"/>
    <path d="M0,79 Q50,81 100,85" fill="none" stroke="url(#swoosh)" vector-effect="non-scaling-stroke" style="stroke-width:4px"/>
  </svg>
  <h2 class="headline">NEW<br>SERVICE</h2>
  <ul class="highlights">
    <li>- Pay Per Performance SEO service</li>
    <li>- Guaranteed Zumbly page 1 ranking</li>
    <li>- Only $197 per month (+ performance bonus)</li>
  </ul>
  <span class="cta">Click here</span>
  <div class="agent-photo" role="img" aria-label="Smiling support agent wearing a headset"></div>
  <div class="brand"><span class="brand-dot"></span>velHelm</div>
</div>

<!-- 336 x 280 -->
<div class="banner rect-large">
  <svg class="banner-bg" viewBox="0 0 100 100" preserveAspectRatio="none" aria-hidden="true">
    <rect width="100" height="100" fill="url(#sky-vertical)"/>
    <path d="M0,72 Q55,90 100,80 L100,100 L0,100Z" fill="#fff"/>
    <path d="M0,72 Q55,90 100,80" fill="none" stroke="url(#swoosh)" vector-effect="non-scaling-stroke" style="stroke-width:3px"/>
  </svg>
  <h2 class="headline">NEW SERVICE</h2>
  <ul class="highlights">
    <li>- Pay Per Performance SEO service</li>
    <li>- Guaranteed Zumbly page 1 ranking</li>
    <li>- Only $197 per month<br>&nbsp;&nbsp;(+ performance bonus)</li>
  </ul>
  <span class="cta">Click here</span>
  <div class="agent-photo" role="img" aria-label="Smiling support agent wearing a headset"></div>
  <div class="brand"><span class="brand-dot"></span>velHelm</div>
</div>

<!-- 300 x 250 -->
<div class="banner rect-medium">
  <svg class="banner-bg" viewBox="0 0 100 100" preserveAspectRatio="none" aria-hidden="true">
    <rect width="100" height="100" fill="url(#sky-vertical)"/>
    <path d="M0,74 Q55,92 100,82 L100,100 L0,100Z" fill="#fff"/>
    <path d="M0,74 Q55,92 100,82" fill="none" stroke="url(#swoosh)" vector-effect="non-scaling-stroke" style="stroke-width:3px"/>
  </svg>
  <h2 class="headline">NEW SERVICE</h2>
  <ul class="highlights">
    <li>- Pay Per Performance<br>&nbsp;&nbsp;SEO service</li>
    <li>- Guaranteed Zumbly page<br>&nbsp;&nbsp;1 ranking</li>
    <li>- Only $197 per month<br>&nbsp;&nbsp;(+ performance bonus)</li>
  </ul>
  <span class="cta">Click here</span>
  <div class="agent-photo" role="img" aria-label="Smiling support agent wearing a headset"></div>
  <div class="brand"><span class="brand-dot"></span>velHelm</div>
</div>

<!-- 250 x 250 -->
<div class="banner square-large">
  <svg class="banner-bg" viewBox="0 0 100 100" preserveAspectRatio="none" aria-hidden="true">
    <rect width="100" height="100" fill="url(#sky-vertical)"/>
    <path d="M0,74 Q55,92 100,82 L100,100 L0,100Z" fill="#fff"/>
    <path d="M0,74 Q55,92 100,82" fill="none" stroke="url(#swoosh)" vector-effect="non-scaling-stroke" style="stroke-width:2.5px"/>
  </svg>
  <h2 class="headline">NEW SERVICE</h2>
  <ul class="highlights">
    <li>- Pay Per Performance SEO service</li>
    <li>- Guaranteed Zumbly page 1 ranking</li>
    <li>- Only $197 per month<br>&nbsp;&nbsp;(+ performance bonus)</li>
  </ul>
  <span class="cta">Click here</span>
  <div class="agent-photo" role="img" aria-label="Smiling support agent wearing a headset"></div>
  <div class="brand"><span class="brand-dot"></span>velHelm</div>
</div>

<!-- 200 x 200 -->
<div class="banner square-small">
  <svg class="banner-bg" viewBox="0 0 100 100" preserveAspectRatio="none" aria-hidden="true">
    <rect width="100" height="100" fill="url(#sky-vertical)"/>
    <path d="M0,74 Q55,92 100,82 L100,100 L0,100Z" fill="#fff"/>
    <path d="M0,74 Q55,92 100,82" fill="none" stroke="url(#swoosh)" vector-effect="non-scaling-stroke" style="stroke-width:2px"/>
  </svg>
  <h2 class="headline">NEW SERVICE</h2>
  <ul class="highlights">
    <li>- Pay Per Performance SEO service</li>
    <li>- Guaranteed Zumbly page 1 ranking</li>
    <li>- Only $197 per month<br>&nbsp;&nbsp;(+ performance bonus)</li>
  </ul>
  <span class="cta">Click here</span>
  <div class="agent-photo" role="img" aria-label="Smiling support agent wearing a headset"></div>
  <div class="brand"><span class="brand-dot"></span>velHelm</div>
</div>

<!-- 728 x 90 -->
<div class="banner leaderboard">
  <svg class="banner-bg" viewBox="0 0 457 58" preserveAspectRatio="none" aria-hidden="true">
    <rect width="457" height="58" fill="#fff"/>
    <rect x="122" width="335" height="58" fill="url(#sky-horizontal)"/>
    <rect x="118" width="4" height="58" fill="url(#brand-stripe)"/>
  </svg>
  <div class="brand"><span class="brand-dot"></span>velHelm</div>
  <h2 class="headline">NEW SERVICE</h2>
  <ul class="highlights">
    <li>- Pay Per Performance SEO service&nbsp; |&nbsp; Guaranteed Zumbly page 1 ranking</li>
    <li>- Only $197 per month (+ performance bonus)</li>
  </ul>
  <span class="cta">Click here</span>
</div>

<!-- 468 x 60 -->
<div class="banner banner-full">
  <svg class="banner-bg" viewBox="0 0 293 39" preserveAspectRatio="none" aria-hidden="true">
    <rect width="293" height="39" fill="#fff"/>
    <rect x="78" width="215" height="39" fill="url(#sky-horizontal)"/>
    <rect x="75" width="3" height="39" fill="url(#brand-stripe)"/>
  </svg>
  <div class="brand"><span class="brand-dot"></span>velHelm</div>
  <h2 class="headline">NEW SERVICE</h2>
  <ul class="highlights">
    <li>- Pay Per Performance SEO service&nbsp; |&nbsp; Guaranteed Zumbly page 1 ranking</li>
    <li>- Only $197 per month (+ performance bonus)</li>
  </ul>
  <span class="cta">Click here</span>
</div>

</body>
</html>
```